Defense contractor needs a roll-up for an exhibition

The booth we have booked has only a size of 3m².
So this will be the centerpiece of the whole booth.
We need a roll-up that attracts visitors and at the same time it should contain already designed graphics. These graphics are giving visitors an overview of our system. So it is necessary to have them exposed in a height that the booth personal can conveniently point with its fingers at them.
For information about our company and product visit:
https://www.brightlanternoptics.com/
For designing you should use Adobe Illustrator and the templates provided in the zip file, to guarantee a perfect print.
I have supplied my business card that you can copy the logo. As the company logo will be already at the booth nearby the top of the roll-up, you should not place it there. It can be in the middle or at the bottom.
I have uploaded a picture of the booth. The roll up will be placed at the left of the screen and has a size of 80cm x 200cm

Defense

Defense

Serif

Colors
0054AA
0677BA
7BADD7
CADEEF
E8F1F8

• you must use the Adobe Illustrator template to have a good printing result
• company logo on the upper side of the roll-up

```html
<!DOCTYPE html>
<html lang="en">
<head>
<meta charset="utf-8">
<title>Advanced Combat Training Systems – Roll-up</title>
<link href="https://fonts.googleapis.com/css2?family=Roboto+Condensed:wght@400;700;800&family=Arimo:wght@400&display=swap" rel="stylesheet">
<style>
  :root {
    --stage: #e4e6ea;
    --banner: #f1f1f3;
    --ink: #1c1c1e;
    --ink-soft: #2a2a2e;
    --rule: #3a3a3e;
    --corner: #7f7d8f;
    --sky-top: #3b3fa8;
    --sky-mid: #8a6fc8;
    --sky-glow: #e59bb0;
    --ground: #0d0d10;
    --inset: #e9e8f0;
    --inset-accent: #8f95d8;
    --room: #d8d6e0;
    --room-accent: #7f86d6;
  }
  html, body {
    margin: 0;
    padding: 0;
    width: 1200px;
    height: 1133px;
    overflow: hidden;
    background: var(--stage);
  }
  .canvas {
    position: relative;
    width: 1200px;
    height: 1133px;
  }
  .rollup {
    position: absolute;
    left: 381px;
    top: 20px;
    width: 437px;
    height: 1093px;
    background: var(--banner);
    overflow: hidden;
    box-shadow: 0 2px 10px rgba(0,0,0,0.12);
  }
  .rollup__graphics {
    position: absolute;
    left: 0;
    top: 0;
    width: 437px;
    height: 600px;
  }
  .headline {
    position: absolute;
    left: 25px;
    top: 622px;
    margin: 0;
    font-family: "Roboto Condensed", "Arial Narrow", sans-serif;
    font-weight: 800;
    font-size: 35px;
    line-height: 38px;
    letter-spacing: 0.2px;
    color: var(--ink);
    text-transform: uppercase;
  }
  .services {
    position: absolute;
    left: 25px;
    top: 786px;
    width: 380px;
  }
  .services__title {
    margin: 0;
    font-family: "Roboto Condensed", "Arial Narrow", sans-serif;
    font-weight: 700;
    font-size: 22px;
    color: var(--ink-soft);
    display: inline-block;
    padding-right: 32px;
    border-bottom: 2px solid var(--rule);
    padding-bottom: 2px;
  }
  .services__intro {
    margin: 10px 0 0;
    font-family: "Roboto Condensed", "Arial Narrow", sans-serif;
    font-weight: 700;
    font-size: 14px;
    line-height: 17px;
    color: var(--ink-soft);
  }
  .services__list {
    list-style: none;
    margin: 10px 0 0;
    padding: 0;
    font-family: "Arimo", Arial, sans-serif;
    font-size: 14.5px;
    line-height: 21px;
    color: var(--ink-soft);
  }
  .services__list li {
    display: flex;
    align-items: center;
    gap: 10px;
  }
  .services__list svg {
    width: 13px;
    height: 13px;
    flex: none;
  }
  .services__closing {
    margin: 12px 0 0;
    font-family: "Roboto Condensed", "Arial Narrow", sans-serif;
    font-weight: 700;
    font-size: 14.5px;
    color: var(--ink-soft);
  }
</style>
</head>
<body>
<main class="canvas">
  <section class="rollup">
    <svg class="rollup__graphics" viewBox="0 0 437 600" xmlns="http://www.w3.org/2000/svg">
      <defs>
        <linearGradient id="skyScene" x1="0" y1="0" x2="0" y2="1">
          <stop offset="0" stop-color="var(--sky-top)"/>
          <stop offset="0.3" stop-color="var(--sky-mid)"/>
          <stop offset="0.5" stop-color="var(--sky-glow)"/>
          <stop offset="0.62" stop-color="var(--ground)"/>
          <stop offset="1" stop-color="var(--ground)"/>
        </linearGradient>
        <linearGradient id="mobileUnit" x1="0" y1="0" x2="1" y2="1">
          <stop offset="0" stop-color="var(--inset)"/>
          <stop offset="1" stop-color="var(--inset-accent)"/>
        </linearGradient>
        <linearGradient id="classroom" x1="0" y1="0" x2="1" y2="1">
          <stop offset="0" stop-color="var(--room)"/>
          <stop offset="1" stop-color="var(--room-accent)"/>
        </linearGradient>
      </defs>
      <circle class="corner-arc" cx="400" cy="20" r="200" fill="var(--corner)"/>
      <circle class="hero-scene" cx="216" cy="212" r="195" fill="url(#skyScene)"
              role="img" aria-label="Photo: tank silhouette against a purple and pink sunset sky"/>
      <path class="classroom-scene" d="M4 470 L230 455 L300 470 L306 594 L4 594 Z" fill="url(#classroom)" opacity="0.85"
            role="img" aria-label="Illustration: training room with wall displays and trainees at desks"/>
      <circle class="mobile-unit" cx="310" cy="365" r="113" fill="url(#mobileUnit)" stroke="var(--ink)" stroke-width="5"
              role="img" aria-label="Illustration: mobile training truck with simulator screens and instructors"/>
    </svg>

    <h1 class="headline">Advanced combat<br>training systems<br>for realistic combat<br>simulation</h1>

    <div class="services">
      <h2 class="services__title">Services</h2>
      <p class="services__intro">The signature of the contract is not the end<br>it is just the beginning of a long-lasting partnership.<br>We offer</p>
      <ul class="services__list">
        <li><svg viewBox="0 0 14 14"><circle cx="7" cy="7" r="6" fill="none" stroke="var(--ink)" stroke-width="1.3"/><path d="M4 7.2 L6.3 9.4 L12 3" fill="none" stroke="var(--ink)" stroke-width="1.6"/></svg>extended warranty programs</li>
        <li><svg viewBox="0 0 14 14"><circle cx="7" cy="7" r="6" fill="none" stroke="var(--ink)" stroke-width="1.3"/><path d="M4 7.2 L6.3 9.4 L12 3" fill="none" stroke="var(--ink)" stroke-width="1.6"/></svg>logistics support</li>
        <li><svg viewBox="0 0 14 14"><circle cx="7" cy="7" r="6" fill="none" stroke="var(--ink)" stroke-width="1.3"/><path d="M4 7.2 L6.3 9.4 L12 3" fill="none" stroke="var(--ink)" stroke-width="1.6"/></svg>maintenance contracts</li>
        <li><svg viewBox="0 0 14 14"><circle cx="7" cy="7" r="6" fill="none" stroke="var(--ink)" stroke-width="1.3"/><path d="M4 7.2 L6.3 9.4 L12 3" fill="none" stroke="var(--ink)" stroke-width="1.6"/></svg>long-term spare part services</li>
      </ul>
      <p class="services__closing">to keep the equipment in perfect operational condition</p>
    </div>
  </section>
</main>
</body>
</html>
```